Velmora Commercial Finance Information Brochure

This brochure will be sent out to clients via A4 PDF on an email to showcase what our company has to offer. We are a commercial finance brokerage, that specialises in property finance. We would like to see designs following our colour scheme. The final design should demonstrate our professionalism and reliability.
I have attached our logo and also a few bullet points on our information and what we can offer. These can be slightly reworded for conciseness. Or leave the text sections as filler and I can fill these in.
I have also attached an overview of our colour scheme and design styling for your consideration.
Target Market(s)
Property Developers
Industry/Entity Type
Financial Services
Look and feel
Each slider illustrates characteristics of the customer's brand and the style your logo design should communicate.

```html
<!DOCTYPE html>
<html lang="en">
<head>
<meta charset="utf-8">
<title>Velmora Finance — Information Brochure</title>
<link href="https://fonts.googleapis.com/css2?family=Mulish:wght@400;600;700;800&display=swap" rel="stylesheet">
<style>
  :root{
    --backdrop:#e4e5e7;
    --paper:#ffffff;
    --brand-blue:#1a4ea1;
    --brand-green:#2a9a4a;
    --ink:#3a3a3a;
    --hex-pale:#e9f4ec;
    --photo-dark:#1b2a48;
    --photo-mid:#3c5d8e;
    --photo-light:#9fb6d3;
  }
  *{margin:0;padding:0;box-sizing:border-box}
  html,body{width:1200px;height:1200px;overflow:hidden}
  body{background:var(--backdrop);font-family:"Mulish",sans-serif;position:relative}
  .brochure{position:absolute;left:182px;top:60px;width:835px;height:1080px;background:var(--paper);overflow:hidden;box-shadow:0 2px 10px rgba(0,0,0,.12)}
  .hero{position:absolute;left:0;top:0;width:835px;height:394px}
  .hero-photo{position:absolute;inset:0;background:linear-gradient(160deg,var(--photo-dark) 0%,var(--photo-mid) 55%,var(--photo-light) 100%)}
  .hero-shapes{position:absolute;inset:0}
  .brand{position:absolute;left:585px;top:92px;width:230px;text-align:center;font-weight:800;font-size:30px;line-height:1.05;color:var(--brand-blue);letter-spacing:1px;text-transform:uppercase}
  .hex-accent{position:absolute;left:0;top:390px}
  .body-copy{position:absolute;left:44px;top:416px;width:748px;color:var(--ink);font-size:13px;line-height:19px;text-align:justify}
  .body-copy p{margin-bottom:16px}
  .footer-wave{position:absolute;left:0;top:905px}
  .footer{position:absolute;left:0;top:938px;width:835px;height:142px;background:var(--brand-blue);color:#fff;font-size:13px}
  .contact-list{position:absolute;left:44px;top:38px;list-style:none;line-height:19.5px}
  .contact-list li{display:flex;align-items:center;gap:7px}
  .contact-list svg{width:11px;height:11px;fill:#fff}
  .footer-divider{position:absolute;left:417px;top:58px;width:1px;height:54px;background:rgba(255,255,255,.7)}
  .address{position:absolute;left:630px;top:66px;line-height:19.5px;font-style:normal}
</style>
</head>
<body>
<main class="brochure">
  <header class="hero">
    <div class="hero-photo" role="img" aria-label="Businessman in a suit touching a rising financial chart over a city skyline"></div>
    <svg class="hero-shapes" viewBox="0 0 835 394" width="835" height="394">
      <polygon points="500,0 835,0 835,230 565,230 470,115" fill="#fff"/>
      <polygon points="514,180 586,180 622,243 586,306 514,306 478,243" fill="#3b5fc4" opacity=".55"/>
      <polygon points="630,222 673,247 673,297 630,322 587,297 587,247" fill="#2a9a4a" opacity=".7"/>
    </svg>
    <div class="brand">Velmora Finance</div>
  </header>

  <svg class="hex-accent" width="140" height="170" viewBox="0 0 140 170">
    <polygon points="0,0 95,0 135,85 95,170 0,170" fill="var(--hex-pale)" opacity=".8"/>
  </svg>

  <section class="body-copy">
    <p>As former lenders and developers ourselves, we intimately understand the inefficiencies that plague deals in the market today. We've experienced the frustration of tight time limits on deals and the exasperating feeling of brokers wasting precious time collecting information. It's enough to drive developers and lenders insane!</p>
    <p>That's why we founded Velmora Finance – to be the efficient and reliable link that connects developers and lenders. We've streamlined our processes to eliminate unnecessary hurdles, enabling clear and swift communication between all parties involved. No more wasted time. No more unnecessary stress.</p>
    <p>With our expertise and industry insights, we've developed a unique approach that simplifies the financing journey. From the initial consultation to the final funding, we're here to guide you every step of the way. Our goal? To make commercial financing a smooth and enjoyable experience for you.</p>
    <p>With our background in the asset management industry, we have cultivated a black book of fund managers, institutions, UHNWI and private equity lenders that we can call on for non-traditional lending.</p>
    <p>Velmora Finance was created to satisfy a need in the market that has been far too overlooked. Efficiency. Efficiency is at the heart of our operations, and we pride ourselves on our ability to secure the best financing options swiftly and effectively for our clients. By employing cutting-edge technology and streamlining our internal processes, we have cultivated a seamless and time-saving approach to finance brokering. Having been a developer, we understand the stresses and headaches associated with building, let alone all the paperwork and emails backwards and forwards between yourself and brokers to attain the necessary financing.</p>
    <p>We are well-versed in the questions lenders will ask, allowing us to get ahead of the curve and request all the necessary information from you on day one. This approach provides you with a distinct advantage, as it eliminates the need to allocate hours each day to answering questions and fulfilling requests from brokers. By entrusting us with this responsibility, you can focus on your core tasks and leave the financing aspect to us, making the process less stressful for you.</p>
  </section>

  <svg class="footer-wave" width="835" height="40" viewBox="0 0 835 40">
    <path d="M0,40 L0,34 C250,30 560,22 835,0 L835,40 Z" fill="var(--brand-green)"/>
    <path d="M0,40 L0,38 C250,36 560,30 835,12 L835,40 Z" fill="#fff"/>
    <path d="M0,40 L0,40 C250,38 560,34 835,18 L835,40 Z" fill="var(--brand-blue)"/>
  </svg>

  <footer class="footer">
    <ul class="contact-list">
      <li><svg viewBox="0 0 24 24"><path d="M6.6 10.8a15 15 0 0 0 6.6 6.6l2.2-2.2a1 1 0 0 1 1-.25 11.4 11.4 0 0 0 3.6.57 1 1 0 0 1 1 1V20a1 1 0 0 1-1 1A17 17 0 0 1 3 4a1 1 0 0 1 1-1h3.5a1 1 0 0 1 1 1c0 1.25.2 2.45.57 3.57a1 1 0 0 1-.25 1z"/></svg>555-014-2287</li>
      <li><svg viewBox="0 0 24 24"><path d="M7 1h10a2 2 0 0 1 2 2v18a2 2 0 0 1-2 2H7a2 2 0 0 1-2-2V3a2 2 0 0 1 2-2zm0 3v14h10V4z"/></svg>555-019-6630</li>
      <li><svg viewBox="0 0 24 24"><path d="M2 5h20v14H2zm2 2v.5l8 5 8-5V7l-8 5z"/></svg>info@velmorafinance.com</li>
      <li><svg viewBox="0 0 24 24"><circle cx="12" cy="12" r="10"/></svg>www.velmorafinance.com</li>
    </ul>
    <div class="footer-divider"></div>
    <address class="address">4120 Larkspur Way<br>Anchorage, Alaska 34571</address>
  </footer>
</main>
</body>
</html>
```